iOS app design for movie reviews app

I need an app redesign for 5 pages of my iphone app. The app is a social movie reviews app that lets you share and find movies based on friends recommendations. The app is currently live in the app store under the working name tomsKit, but I will be re-branding under the name "glinted". Reviews will now be called "quips". The app is free in the app store and is a good reference for the functionality. Some screenshots can be seen here: https://apps.example-store.test/us/app/tomskit/id902716453?mt=8
The 5 pages should have a similar look and feel and do not have to match what is currently live in the app store. I am looking to do an overhaul of the design and am open to completely new designs, this includes color scheme.
1. Splash Screen - page users see when they initially open the app to login. Should include the name of the app (glinted) and login with facebook button, as well as graphics or a logo. Current design should be ignored.
2. Home Page (screenshot #2 on itunes page) - page user sees when they login after their first session. This is where users will normally land and is the primary place users navigate the app. The homepage must have a few elements: searchbar to find movies, user stats (quips, followers, # of time other users have read your quips, # of times other users have viewed your profile page), and six icons to navigate (watchlist, explore, popular, messages, network and my reviews). Watchlist, messages and network icons will have notification messages that come up to show when the user has new activity on those pages. There are currently icons for some of these in the app, but I am open to redesigns of these as well
3. Movie Profile Page - this is a new page to the app where a user can see more detailed information about a specific movie. This page must include poster image, title, genre, release date, rating (PG, R, etc.), length, description, video trailer and actors. A user will get to this page by tapping on the short description on the movie page (screenshot #1 on itunes page) above their friends reviews. This page will not have any reviews, just details about the movie.
4. Explore Page - this is the page where users can perform a specific search for movies. There are two filters that need to be accessible (location of movie and genre). A user can perform a search just for themself and filter by movies they have seen or never seen. They can also search for movies that they want to watch with a friend, so they select a friend and see results that both of them would like.
5. My Reviews Page (screenshot #4 on itunes page)- this page shows all the reviews (quips) that a user has submitted. This is just their number rating as well as the number of views that review has collected from other users. They can be sorted by top rated or most viewed.
Optional: I will also need an app icon that matches the look and feel of the app.

```html
<!DOCTYPE html>
<html lang="en">
<head>
<meta charset="utf-8">
<title>glinted – Home and Result screens</title>
<link href="https://fonts.googleapis.com/css2?family=Arimo:ital,wght@0,400;0,700;1,400&display=swap" rel="stylesheet">
<style>
:root{
  --stage:#e6e6e6;
  --status:#0d0d0d;
  --red-top:#b3252a;
  --red-bottom:#7c1114;
  --stitch:#e59a9a;
  --light:#e3e3e3;
  --lighter:#efefef;
  --dark:#2b2b2b;
  --darker:#1f1f1f;
  --white:#ffffff;
  --ink:#333333;
  --muted:#777777;
  --stat-red:#b51d22;
  --genre-red:#d4141a;
  --green:#5a9a1e;
  --blue:#2f79c9;
  --teal:#6fb3a6;
  --orange:#f0a028;
  --icon-ring:#b9b7b2;
  --icon-fill:#8d8a84;
  --photo-warm:#7a5a4a;
  --photo-cool:#3a5f86;
}
*{box-sizing:border-box;margin:0;padding:0}
html,body{width:1200px;height:849px;overflow:hidden;background:var(--stage)}
body{font-family:"Arimo",Helvetica,Arial,sans-serif}
.stage{position:absolute;left:0;top:0;width:1169px;height:827px;transform:scale(1.0265);transform-origin:0 0}
.screen{position:absolute;top:68px;width:467px;height:704px;overflow:hidden;background:var(--light)}
.screen--home{left:66px}
.screen--result{left:639px;background:var(--darker)}
.abs{position:absolute}

.status-bar{left:0;top:0;width:100%;height:32px;background:var(--status);color:var(--white);font-weight:700;font-size:19px}
.status-bar .carrier{left:40px;top:6px}
.status-bar svg{position:absolute}

.app-header{left:0;top:32px;width:100%;height:65px;background:linear-gradient(var(--red-top),var(--red-bottom))}
.app-header::after{content:"";position:absolute;left:0;right:0;bottom:6px;border-top:1px dashed var(--stitch);opacity:.7}
.app-title{left:0;right:0;top:14px;text-align:center;color:var(--white);font-size:28px;font-weight:700}

/* home */
.search-band{left:0;top:97px;width:100%;height:66px;background:linear-gradient(var(--lighter),#cfcfcf)}
.search-field{left:18px;top:12px;width:431px;height:34px;border-radius:17px;background:linear-gradient(#d6d6d6,#ececec);border:1px solid #9a9a9a;box-shadow:inset 0 2px 3px rgba(0,0,0,.25)}
.search-field span{position:absolute;left:36px;top:8px;font-size:15px;font-weight:700;color:#555}
.search-field svg{position:absolute;left:13px;top:9px}
.profile-band{left:0;top:163px;width:100%;height:62px;background:var(--dark)}
.avatar{left:15px;top:173px;width:140px;height:140px;border-radius:8px;border:2px solid #555;box-shadow:0 2px 6px rgba(0,0,0,.5);background:linear-gradient(135deg,var(--photo-warm),#2a1f1c)}
.user-name{left:174px;top:190px;color:var(--white);font-size:20px;font-weight:700;letter-spacing:.3px}
.stats{left:155px;top:225px;width:312px;height:60px;background:var(--lighter);display:flex}
.stat{flex:1;border-left:1px solid #cfcfcf;text-align:center;padding-top:8px}
.stat b{display:block;color:var(--stat-red);font-size:24px}
.stat span{font-size:13px;color:var(--muted)}
.progress{left:212px;top:302px;width:149px;height:11px;border-radius:6px;background:#1c1c1c}
.progress i{position:absolute;left:2px;top:2px;width:66px;height:7px;border-radius:4px;background:var(--green)}
.progress-label{left:370px;top:298px;font-size:19px;color:#444}
.divider{left:16px;top:333px;width:436px;border-top:1px solid #c9c9c9}
.nav-item{width:120px;text-align:center;font-size:15px;font-weight:700;color:#444}
.nav-icon{display:block;margin:0 auto 12px;width:72px;height:72px;border-radius:50%;background:radial-gradient(circle at 50% 35%,#dedcd8,var(--icon-ring));border:3px solid #f4f4f4;box-shadow:0 3px 5px rgba(0,0,0,.35)}
.nav-icon svg{margin-top:17px}
.badge{position:absolute;left:108px;top:522px;width:25px;height:25px;border-radius:5px;background:#c8161c;color:var(--white);font-size:16px;font-weight:700;text-align:center;line-height:25px}

/* result */
.btn-back{left:12px;top:13px;width:60px;height:36px;border-radius:6px;background:#8f1519;border:1px solid #5e0b0d;color:var(--white);font-weight:700;font-size:16px;text-align:center;line-height:34px}
.btn-home{left:412px;top:13px;width:38px;height:36px;border-radius:6px;background:#8f1519;border:1px solid #5e0b0d}
.btn-home svg{margin:7px 0 0 7px}
.match-band{left:0;top:97px;width:100%;height:88px;background:var(--dark)}
.match-title{left:12px;top:20px;color:var(--white);font-size:19px;font-weight:700}
.match-sub{left:12px;top:50px;color:#bbb;font-size:16px;font-style:italic}
.match-photo{top:10px;width:70px;height:70px;border-radius:6px;border:2px solid #555}
.tabs{left:0;top:185px;width:100%;height:57px;background:linear-gradient(#f0f0f0,#c9c9c9)}
.tab{top:10px;height:37px;border-radius:5px;font-size:12px;text-align:center;line-height:33px}
.tab--off{left:83px;width:130px;background:#e9e9e9;border:2px solid #aaa;color:#777}
.tab--on{left:271px;width:113px;background:var(--blue);border:2px solid #a9c6dd;color:var(--white)}
.list-panel{left:24px;top:242px;width:420px;height:470px;background:#2c2c2c;box-shadow:inset 0 0 8px rgba(0,0,0,.8)}
.shelf{left:4px;width:459px;height:18px;background:linear-gradient(#a3d9cd,var(--teal) 45%,#3e7268);border-radius:2px}
.poster{left:38px;width:102px;height:150px;border:1px solid #111}
.movie-title{left:152px;color:var(--white);font-size:19px;font-weight:700}
.movie-genre{left:152px;color:var(--genre-red);font-size:13px;font-style:italic}
.movie-cast{left:152px;color:#ccc;font-size:13px;font-style:italic}
.row-label{left:152px;color:var(--white);font-size:15px}
.flag{left:208px;width:14px;height:18px}
.slot{left:232px;width:36px;height:18px;border-radius:3px;background:#161616}
.score{left:275px;width:35px;height:18px;border-radius:3px;background:var(--blue);color:var(--white);font-size:12px;font-weight:700;text-align:center;line-height:18px}
.reviews{left:318px;color:#bbb;font-size:12px;font-style:italic}
</style>
</head>
<body>
<div class="stage">

  <!-- Home screen -->
  <section class="screen screen--home">
    <div class="abs status-bar">
      <svg style="left:10px;top:9px" width="28" height="14"><g fill="#fff"><rect x="0" y="10" width="3" height="4"/><rect x="5" y="8" width="3" height="6"/><rect x="10" y="5" width="3" height="9"/><rect x="15" y="2" width="3" height="12"/><rect x="20" y="0" width="3" height="14"/></g></svg>
      <span class="abs carrier">NIMBUS&nbsp; 3G</span>
      <svg style="left:225px;top:6px" width="16" height="20"><path d="M4 9V6a4 4 0 0 1 8 0v3" stroke="#fff" stroke-width="2" fill="none"/><rect x="1" y="9" width="14" height="10" rx="1" fill="#fff"/></svg>
      <svg style="left:432px;top:9px" width="30" height="14"><rect x="1" y="1" width="25" height="12" rx="2" stroke="#fff" stroke-width="1.5" fill="none"/><rect x="3" y="3" width="21" height="8" fill="#fff"/><rect x="27" y="4" width="2" height="6" fill="#fff"/></svg>
    </div>
    <header class="abs app-header"><div class="abs app-title">glinted</div></header>

    <div class="abs search-band">
      <div class="abs search-field">
        <svg width="16" height="16"><circle cx="6" cy="6" r="4.5" stroke="#555" stroke-width="2" fill="none"/><path d="M9.5 9.5l5 5" stroke="#555" stroke-width="2.5"/></svg>
        <span>Search Movie</span>
      </div>
    </div>

    <div class="abs profile-band"></div>
    <div class="abs user-name">Marina Holt</div>
    <div class="abs stats">
      <div class="stat"><b>9</b><span>Quips</span></div>
      <div class="stat"><b>12</b><span>Followers</span></div>
      <div class="stat"><b>2</b><span>Views</span></div>
    </div>
    <div class="abs avatar" role="img" aria-label="User profile photo"></div>
    <div class="abs progress"><i></i></div>
    <div class="abs progress-label">30%</div>
    <div class="abs divider"></div>

    <div class="abs nav-item" style="left:29px;top:372px"><span class="nav-icon"><svg width="34" height="34" viewBox="0 0 34 34"><rect x="3" y="5" width="28" height="26" rx="3" fill="var(--icon-fill)"/><g fill="#d8d6d2"><rect x="8" y="13" width="18" height="3"/><rect x="8" y="19" width="18" height="3"/><rect x="8" y="25" width="18" height="3"/></g><rect x="9" y="2" width="3" height="6" fill="var(--icon-fill)"/><rect x="22" y="2" width="3" height="6" fill="var(--icon-fill)"/></svg></span>Watchlist</div>
    <div class="abs nav-item" style="left:172px;top:372px"><span class="nav-icon"><svg width="34" height="34"><circle cx="20" cy="13" r="9" stroke="var(--icon-fill)" stroke-width="4" fill="none"/><path d="M13 20L4 30" stroke="var(--icon-fill)" stroke-width="5" stroke-linecap="round"/></svg></span>Explore</div>
    <div class="abs nav-item" style="left:316px;top:372px"><span class="nav-icon"><svg width="34" height="34" viewBox="0 0 34 34"><path d="M17 2l4.6 9.5 10.4 1.4-7.6 7.2 1.9 10.3L17 25.4 7.7 30.4l1.9-10.3L2 12.9l10.4-1.4z" fill="var(--icon-fill)"/></svg></span>Popular</div>
    <div class="abs nav-item" style="left:29px;top:526px"><span class="nav-icon"><svg width="34" height="34"><circle cx="12" cy="11" r="6" fill="var(--icon-fill)"/><path d="M1 30c0-8 5-12 11-12s11 4 11 12z" fill="var(--icon-fill)"/><circle cx="23" cy="10" r="5" fill="#a6a39d"/><path d="M22 17c6 0 11 3 11 11h-8c0-5-2-8-5-10z" fill="#a6a39d"/></svg></span>My Network</div>
    <div class="badge">3</div>
    <div class="abs nav-item" style="left:172px;top:526px"><span class="nav-icon"><svg width="34" height="34"><path d="M2 7c5-2 10-2 15 2v20c-5-4-10-4-15-2z M32 7c-5-2-10-2-15 2v20c5-4 10-4 15-2z" fill="none" stroke="var(--icon-fill)" stroke-width="2.5" stroke-linejoin="round"/><g stroke="var(--icon-fill)" stroke-width="1.5"><path d="M6 13h7M6 17h7M6 21h7M21 13h7M21 17h7M21 21h7"/></g></svg></span>My Quips</div>
    <div class="abs nav-item" style="left:316px;top:526px"><span class="nav-icon"><svg width="34" height="34" viewBox="0 0 34 34"><g fill="var(--icon-fill)"><circle cx="17" cy="17" r="11"/><rect x="14" y="1" width="6" height="32" rx="1"/><rect x="1" y="14" width="32" height="6" rx="1"/><rect x="14" y="1" width="6" height="32" rx="1" transform="rotate(45 17 17)"/><rect x="14" y="1" width="6" height="32" rx="1" transform="rotate(-45 17 17)"/></g><circle cx="17" cy="17" r="5" fill="#d8d6d2"/></svg></span>Settings</div>
  </section>

  <!-- Result screen -->
  <section class="screen screen--result">
    <div class="abs status-bar">
      <svg style="left:10px;top:9px" width="28" height="14"><g fill="#fff"><rect x="0" y="10" width="3" height="4"/><rect x="5" y="8" width="3" height="6"/><rect x="10" y="5" width="3" height="9"/><rect x="15" y="2" width="3" height="12"/><rect x="20" y="0" width="3" height="14"/></g></svg>
      <span class="abs carrier">NIMBUS&nbsp; 3G</span>
      <svg style="left:225px;top:6px" width="16" height="20"><path d="M4 9V6a4 4 0 0 1 8 0v3" stroke="#fff" stroke-width="2" fill="none"/><rect x="1" y="9" width="14" height="10" rx="1" fill="#fff"/></svg>
      <svg style="left:432px;top:9px" width="30" height="14"><rect x="1" y="1" width="25" height="12" rx="2" stroke="#fff" stroke-width="1.5" fill="none"/><rect x="3" y="3" width="21" height="8" fill="#fff"/><rect x="27" y="4" width="2" height="6" fill="#fff"/></svg>
    </div>
    <header class="abs app-header">
      <div class="abs app-title">result</div>
      <div class="abs btn-back">Back</div>
      <div class="abs btn-home"><svg width="24" height="22"><path d="M12 2L1 12h3v9h6v-6h4v6h6v-9h3z" fill="#fff"/></svg></div>
    </header>

    <div class="abs match-band">
      <div class="abs match-title">Best Mach:</div>
      <div class="abs match-sub">All Genres and In Theaters</div>
      <div class="abs match-photo" style="left:271px;background:linear-gradient(135deg,var(--photo-warm),#2a1f1c)" role="img" aria-label="Your profile photo"></div>
      <div class="abs match-photo" style="left:373px;background:linear-gradient(135deg,var(--photo-cool),#1c2a3a)" role="img" aria-label="Matched friend profile photo"></div>
    </div>

    <div class="abs tabs">
      <div class="abs tab tab--off">Movies with reviews</div>
      <div class="abs tab tab--on">Others Movies</div>
    </div>

    <div class="abs list-panel"></div>

    <!-- movie 1 -->
    <div class="abs poster" style="top:250px;background:linear-gradient(160deg,#c7742f,#5a2a18 60%,#1d1d1d)" role="img" aria-label="Movie poster: Steel Warden 3"></div>
    <div class="abs movie-title" style="top:252px">Steel Warden 3 (2013)</div>
    <div class="abs movie-genre" style="top:276px">Action | Adventure | Sci-Fi</div>
    <div class="abs movie-cast" style="top:300px">Victor Hale Jr., Renata Palmer, Dom.......</div>
    <div class="abs row-label" style="top:330px">You:</div>
    <svg class="abs flag" style="top:330px"><path d="M0 0h14v18l-7-5-7 5z" fill="var(--orange)"/></svg>
    <div class="abs slot" style="top:330px"></div><div class="abs score" style="top:330px">9.5</div><div class="abs reviews" style="top:332px">5 review</div>
    <div class="abs row-label" style="top:367px">Friend:</div>
    <svg class="abs flag" style="top:367px"><path d="M0 0h14v18l-7-5-7 5z" fill="#111"/></svg>
    <div class="abs slot" style="top:367px"></div><div class="abs score" style="top:367px">7.5</div><div class="abs reviews" style="top:369px">2 review</div>
    <div class="abs shelf" style="top:395px"></div>

    <!-- movie 2 -->
    <div class="abs poster" style="top:434px;background:linear-gradient(#cfe7f3,#eef3ea 60%,#6b8a5a)" role="img" aria-label="Movie poster: The Quiet Tutor"></div>
    <div class="abs movie-title" style="top:437px">The Quiet Tutor (2013)</div>
    <div class="abs movie-genre" style="top:461px">Comedy | Drama</div>
    <div class="abs movie-cast" style="top:485px">Lena Carver, Julia Morrow, Milo Anders.....</div>
    <div class="abs row-label" style="top:515px">You:</div>
    <svg class="abs flag" style="top:515px"><path d="M0 0h14v18l-7-5-7 5z" fill="var(--orange)"/></svg>
    <div class="abs slot" style="top:515px"></div><div class="abs score" style="top:515px">7.5</div><div class="abs reviews" style="top:517px">5 review</div>
    <div class="abs row-label" style="top:552px">Friend:</div>
    <svg class="abs flag" style="top:552px"><path d="M0 0h14v18l-7-5-7 5z" fill="var(--orange)"/></svg>
    <div class="abs slot" style="top:552px"></div><div class="abs score" style="top:552px">6.5</div><div class="abs reviews" style="top:554px">2 review</div>
    <div class="abs shelf" style="top:580px"></div>

    <!-- movie 3 -->
    <div class="abs poster" style="top:619px;background:linear-gradient(#3a4f7a,#8a5a48 55%,#2a2a2a)" role="img" aria-label="Movie poster: Grit &amp; Glory"></div>
    <div class="abs movie-title" style="top:622px">Grit &amp; Glory (2013)</div>
    <div class="abs movie-genre" style="top:646px">Comedy | Crime | Drama</div>
    <div class="abs movie-cast" style="top:670px">Mark Walden, Dwight Jensen, Andrew.......</div>
    <div class="abs row-label" style="top:699px">You:</div>
    <svg class="abs flag" style="top:699px"><path d="M0 0h14v18l-7-5-7 5z" fill="var(--orange)"/></svg>
    <div class="abs slot" style="top:699px"></div><div class="abs score" style="top:699px">8.0</div>
  </section>

</div>
</body>
</html>
```